Bakery Business Cards

We are in need of business cards for our bakery business--something non-generic that reflects our business and will stand out. We are a wholesale bakery that primarily services in-store bakeries, casinos, schools, distributors, and fund-raising companies. The family business was founded in 1960. (www.dorvalbakehouse.example)

```html
<!DOCTYPE html>
<html lang="en">
<head>
<meta charset="utf-8">
<title>Dorval Bakehouse Business Cards</title>
<link href="https://fonts.googleapis.com/css2?family=Libre+Baskerville:wght@400;700&display=swap" rel="stylesheet">
<style>
  :root {
    --maroon: #7a1a24;
    --gold: #e0a63a;
    --white: #ffffff;
    --page: #f4f2ef;
    --wood-dark: #c9a46e;
    --wood-light: #e2cda6;
  }
  * { box-sizing: border-box; margin: 0; padding: 0; }
  html, body { width: 1200px; height: 1200px; overflow: hidden; }
  body {
    background: var(--page);
    font-family: "Libre Baskerville", Georgia, serif;
    position: relative;
  }
  .card {
    position: absolute;
    left: 200px;
    width: 800px;
    height: 457px;
    background: var(--white);
    overflow: hidden;
    box-shadow: 0 10px 28px rgba(0,0,0,0.18);
  }
  .card--front { top: 110px; }
  .card--back { top: 633px; }

  .photo-area {
    background: linear-gradient(135deg, var(--wood-dark), var(--wood-light));
  }

  /* front */
  .front-photo {
    position: absolute; left: 0; top: 0; width: 330px; height: 100%;
  }
  .front-band {
    position: absolute; left: 346px; top: 0; width: 74px; height: 100%;
    background: var(--maroon);
  }
  .contact-icon {
    position: absolute; left: 13px; width: 48px; height: 48px;
    border-radius: 50%; background: var(--white);
    display: flex; align-items: center; justify-content: center;
  }
  .front-brand {
    position: absolute; left: 440px; right: 30px; top: 48px;
    text-align: center; color: var(--gold);
  }
  .front-brand .brand-name { font-size: 34px; font-weight: 700; line-height: 1.1; }
  .front-brand .brand-since { font-size: 14px; letter-spacing: 1px; margin-top: 6px; }
  .contact-list {
    position: absolute; left: 450px; top: 0; right: 20px;
    list-style: none; color: var(--maroon); font-size: 19px;
  }
  .contact-list li { position: absolute; left: 0; white-space: nowrap; line-height: 1.35; }

  /* back */
  .back-photo { position: absolute; inset: 0; }
  .back-oval {
    position: absolute; left: 225px; top: 80px; width: 370px; height: 210px;
    border-radius: 50%; background: var(--white);
    display: flex; flex-direction: column; align-items: center; justify-content: center;
    color: var(--maroon); text-align: center;
  }
  .back-oval .brand-name { font-size: 38px; font-weight: 700; line-height: 1.1; }
  .back-oval .brand-since { font-size: 16px; letter-spacing: 1px; margin-top: 8px; }
  .back-band {
    position: absolute; left: 0; bottom: 0; width: 100%; height: 92px;
    background: var(--maroon); color: var(--white);
    display: flex; align-items: center; justify-content: center;
    font-size: 20px;
  }
</style>
</head>
<body>

<section class="card card--front">
  <div class="front-photo photo-area" role="img" aria-label="Overhead photo of fruit pies and cobblers on white plates on a wooden table"></div>
  <div class="front-band">
    <span class="contact-icon" style="top:128px">
      <svg width="24" height="24" viewBox="0 0 24 24"><path d="M6.6 10.8a15 15 0 0 0 6.6 6.6l2.2-2.2a1 1 0 0 1 1-.25 11.4 11.4 0 0 0 3.6.57 1 1 0 0 1 1 1V20a1 1 0 0 1-1 1A17 17 0 0 1 3 4a1 1 0 0 1 1-1h3.5a1 1 0 0 1 1 1c0 1.25.2 2.45.57 3.57a1 1 0 0 1-.25 1z" fill="var(--gold)"/></svg>
    </span>
    <span class="contact-icon" style="top:196px">
      <svg width="26" height="20" viewBox="0 0 26 20"><rect x="1" y="1" width="24" height="18" fill="none" stroke="var(--gold)" stroke-width="1.8"/><path d="M1 1l12 10L25 1M1 19l9-8M25 19l-9-8" fill="none" stroke="var(--gold)" stroke-width="1.6"/></svg>
    </span>
    <span class="contact-icon" style="top:264px">
      <svg width="28" height="28" viewBox="0 0 28 28" fill="none" stroke="var(--gold)" stroke-width="1.6"><circle cx="14" cy="14" r="12"/><ellipse cx="14" cy="14" rx="5.5" ry="12"/><path d="M2 14h24M4 8h20M4 20h20M14 2v24"/></svg>
    </span>
    <span class="contact-icon" style="top:332px">
      <svg width="22" height="28" viewBox="0 0 22 28"><path d="M11 1a10 10 0 0 0-10 10c0 7.5 10 16 10 16s10-8.5 10-16A10 10 0 0 0 11 1z" fill="var(--gold)"/><circle cx="11" cy="11" r="3.8" fill="var(--white)"/></svg>
    </span>
  </div>
  <div class="front-brand">
    <div class="brand-name">Dorval Bakehouse</div>
    <div class="brand-since">SINCE 1960</div>
  </div>
  <ul class="contact-list">
    <li style="top:138px">555.014.2837</li>
    <li style="top:206px">hello@dorvalbakehouse.example</li>
    <li style="top:274px">www.dorvalbakehouse.example</li>
    <li style="top:330px">1187 Millstone Rd<br>Harlow Springs, OK 73999</li>
  </ul>
</section>

<section class="card card--back">
  <div class="back-photo photo-area" role="img" aria-label="Overhead photo of pie slices and fruit cobblers on white plates on a wooden table"></div>
  <div class="back-oval">
    <div class="brand-name">Dorval<br>Bakehouse</div>
    <div class="brand-since">SINCE 1960</div>
  </div>
  <div class="back-band">www.dorvalbakehouse.example</div>
</section>

</body>
</html>
```